Business Card design for insurance broker in Denver, CO, USA

I need a business card designed using this logo that was just created. We sell life and disability income insurance to US consumers.
Looking for a professionally designed card to make use of the logo and have something to hand to prospects or new business referral sources. The card could be white, gray, black or whatever you would recommend.

Target Market(s)

US Consumers and other financial professionals that I partner with.

Industry/Entity Type

Insurance Broker

Contact Information for Business Card

Warren T. Holby, CLU, LUTCF (please note that CLU should have a superscript R in a circle for registered trademark)
President
phone (303) 555-0174
email warren@kestrelcoverageplans.example
4620 W. Calloway Rd, Suite 300, Greenwood Village, CO 80112
Somewhere fit in a tagline saying "Your resource for life, long term care, and disability insurance" (maybe the back if it doesn't fit on the front, your call)

Font styles to use
Sans Serif

Requirements
Must have
• Must have logo in correct blue and gray colors, my name, address, phone, email. Order and placement determined by the designer.
• I just want something that looks a more professional than what I could have done using the business card designer tool on printnook.example or CardHatch, or any other do-it-yourself tool
• A regular rectangular business card with square corners is preferred
Nice to have
• I included the logos of 2 organizations I belong to (QWBS and BOLKE). They should be small, but visible on the back only. If it doesn’t look good, this is not a requirement, feel free to drop it.
Should not have
• Do not add any colors not already in the logo, except use of black and whites which are okay. If you use the logo on the back and want to make that in all black, gray or white, that may be okay as well.

```html
<!DOCTYPE html>
<html lang="en">
<head>
<meta charset="utf-8">
<title>Kestrel Coverage Plans – Business Card</title>
<link rel="stylesheet" href="https://fonts.googleapis.com/css2?family=Montserrat:wght@500;600;700&display=swap">
<style>
  :root {
    --brand-blue: #1e88c7;
    --brand-gray: #9a9a9a;
    --paper: #ffffff;
    --backdrop: #ededed;
  }
  html, body {
    margin: 0;
    padding: 0;
    width: 1200px;
    height: 1200px;
    overflow: hidden;
    background: var(--backdrop);
  }
  .stage { display: block; width: 1200px; height: 1200px; }
  .card-face { fill: var(--paper); }
  .card-back { fill: var(--brand-blue); }
  .brand-ring { fill: none; stroke: var(--brand-blue); stroke-width: 5; }
  .brand-name {
    font-family: "Montserrat", sans-serif;
    font-weight: 700;
    fill: var(--brand-blue);
    letter-spacing: 0.5px;
  }
  .rule { stroke: var(--brand-blue); stroke-width: 3; }
  .holder-name {
    font-family: "Montserrat", sans-serif;
    font-weight: 700;
    font-size: 29px;
    fill: var(--brand-blue);
  }
  .credentials {
    font-family: "Montserrat", sans-serif;
    font-weight: 600;
    font-size: 20px;
    fill: var(--brand-gray);
  }
  .credentials .role { fill: var(--brand-blue); }
  .credentials .mark { font-size: 9px; }
  .contact {
    font-family: "Montserrat", sans-serif;
    font-weight: 600;
    font-size: 14.5px;
    fill: var(--brand-gray);
  }
  .address {
    font-family: "Montserrat", sans-serif;
    font-weight: 500;
    font-size: 15px;
    fill: var(--brand-gray);
  }
  .icon { fill: var(--brand-blue); }
  .icon-line { fill: none; stroke: var(--brand-blue); stroke-width: 1.6; }
  .back-ring { fill: none; stroke: var(--paper); stroke-width: 6; }
  .back-name {
    font-family: "Montserrat", sans-serif;
    font-weight: 700;
    font-size: 34px;
    fill: var(--paper);
    letter-spacing: 2px;
  }
  .tagline {
    font-family: "Montserrat", sans-serif;
    font-weight: 600;
    font-size: 19px;
    fill: var(--paper);
    letter-spacing: 1.6px;
  }
</style>
</head>
<body>
<svg class="stage" viewBox="0 0 1200 1200" xmlns="http://www.w3.org/2000/svg">

  <!-- Front of card -->
  <g class="card card--front" transform="translate(235,170)">
    <rect class="card-face" width="701" height="377"/>

    <g class="brand-lockup">
      <circle class="brand-ring" cx="62" cy="192" r="40"/>
      <text class="brand-name" x="118" y="186" font-size="26">KESTREL</text>
      <text class="brand-name" x="118" y="214" font-size="19">COVERAGE PLANS</text>
    </g>

    <line class="rule" x1="333" y1="67" x2="333" y2="310"/>

    <g class="identity">
      <text class="holder-name" x="360" y="92">WARREN T. HOLBY</text>
      <text class="credentials" x="362" y="118">CLU<tspan class="mark" dy="-10">®</tspan><tspan dy="10">, LUTCF </tspan><tspan class="role">President</tspan></text>
    </g>

    <g class="contact-list">
      <g class="icon-phone" transform="translate(372,171)">
        <path class="icon" d="M-14,-4 q14,-10 28,0 l-3,5 q-11,-6 -22,0 z"/>
        <rect class="icon" x="-9" y="-1" width="18" height="10" rx="3"/>
        <circle cx="0" cy="4" r="3" fill="#fff"/>
      </g>
      <text class="contact" x="391" y="176">(303) 555-0174</text>

      <g class="icon-mail" transform="translate(372,202)">
        <rect class="icon-line" x="-10" y="-7" width="20" height="14"/>
        <path class="icon-line" d="M-10,-7 L0,2 L10,-7 M-10,7 L-3,0 M10,7 L3,0"/>
      </g>
      <text class="contact" x="391" y="207">warren@kestrelcoverageplans.example</text>

      <g class="icon-web" transform="translate(372,235)">
        <circle class="icon" r="11"/>
        <ellipse cx="0" cy="0" rx="4.5" ry="11" fill="none" stroke="#fff" stroke-width="1.2"/>
        <line x1="-11" y1="0" x2="11" y2="0" stroke="#fff" stroke-width="1.2"/>
      </g>
      <text class="contact" x="391" y="240">www.kestrelcoverageplans.example</text>
    </g>

    <g class="postal">
      <text class="address" x="357" y="288">4620 W. Calloway Rd, Suite 300,</text>
      <text class="address" x="357" y="308">Greenwood Village, CO 80112</text>
    </g>
  </g>

  <!-- Back of card -->
  <g class="card card--back" transform="translate(235,636)">
    <rect class="card-back" width="701" height="377"/>
    <circle class="back-ring" cx="351" cy="120" r="62"/>
    <text class="back-name" x="351" y="240" text-anchor="middle">KESTREL COVERAGE PLANS</text>
    <text class="tagline" x="351" y="317" text-anchor="middle">YOUR RESOURCE FOR LIFE, LONG TERM CARE,</text>
    <text class="tagline" x="351" y="342" text-anchor="middle">AND DISABILITY INSURANCE</text>
  </g>
</svg>
</body>
</html>
```